Simple, elegant, business card design required

Hi designers,I am looking for a simple yet elegant business card design.

Please make use of my logo (attached); you are free to tweak the logo should you wish to do so.

Our business is involved in many different fields - almost all of them involved in some form of "design", so that's really one of the key things I want to portray. I do not wish to specify which field of design, exactly.

I prefer white on black (or just monochromatic), but if you have a different, creative idea, I am open to that too.

You can use artsy photographs provided that you have the license to use those. Please feel free to ask me any questions.

Target Market(s)

High-end customers looking for design consultancy

Industry/Entity Type

Business

Contact Information for Business Card

Name: Gareth Pellwinter
Position: Creative Director
Mobile: +150963218745
Address: Morrow Lane, Stratford upon Avon, Warwickshire CV37 2JT
Website: corvastudio.com (not launched yet)

Requirements
Must have
• Design layout must be clean, original, and text must be readable when printed.
Should not have
• ~ No business card templates please. Anyone using this will be reported.
• ~ Please don't spam entries.

```html
<!DOCTYPE html>
<html lang="en">
<head>
<meta charset="utf-8">
<title>Corva Studio — Business Card</title>
<link rel="stylesheet" href="https://fonts.googleapis.com/css2?family=Antonio:wght@400&family=Roboto:wght@400&display=swap">
<style>
  :root {
    --stage: #8a8a8a;
    --card-white: #ffffff;
    --card-black: #000000;
    --ink: #111111;
    --contact-grey: #b5b5b5;
    --icon-grey: #6a6a6a;
  }
  * { margin: 0; padding: 0; box-sizing: border-box; }
  html, body {
    width: 1200px; height: 901px; overflow: hidden;
    background: var(--stage);
  }
  .card {
    position: absolute; left: 100px; top: 165px;
    width: 1000px; height: 570px;
    background: var(--card-white);
    box-shadow: 0 18px 40px rgba(0,0,0,0.35);
    overflow: hidden;
  }
  .card__contact-band {
    position: absolute; left: 0; top: 330px;
    width: 100%; height: 240px;
    background: var(--card-black);
  }
  .card__mark {
    position: absolute; left: 120px; top: 0;
    width: 250px; height: 250px;
    background: var(--card-black);
    box-shadow: 6px 8px 14px rgba(0,0,0,0.45);
  }
  .card__brand {
    position: absolute; left: 410px; top: 108px;
    font-family: "Antonio", sans-serif; font-weight: 400;
    font-size: 68px; line-height: 1;
    letter-spacing: 0.18em; color: var(--ink);
    text-transform: uppercase; white-space: nowrap;
  }
  .card__person {
    position: absolute; left: 118px; top: 262px;
    font-family: "Roboto", sans-serif; color: var(--ink);
  }
  .card__name { font-size: 30px; line-height: 1.1; }
  .card__role { font-size: 20px; line-height: 1.2; padding-left: 30px; }
  .contact {
    position: absolute; display: flex; align-items: center; gap: 16px;
    font-family: "Roboto", sans-serif; font-size: 26px;
    color: var(--contact-grey); white-space: nowrap;
  }
  .contact svg { width: 24px; height: 28px; flex: none; }
  .contact--address { left: 54px; top: 380px; }
  .contact--phone { left: 54px; top: 446px; }
  .contact--web { left: 340px; top: 458px; gap: 30px; }
</style>
</head>
<body>
  <article class="card">
    <div class="card__contact-band"></div>
    <div class="card__mark" aria-hidden="true"></div>
    <h1 class="card__brand">Corva Studio</h1>
    <div class="card__person">
      <p class="card__name">Gareth Pellwinter</p>
      <p class="card__role">Creative Director</p>
    </div>

    <p class="contact contact--address">
      <svg viewBox="0 0 24 28" aria-hidden="true"><path d="M12 2a8 8 0 0 0-8 8c0 6 8 15 8 15s8-9 8-15a8 8 0 0 0-8-8z" fill="none" stroke="var(--icon-grey)" stroke-width="2.4"/><circle cx="12" cy="10" r="3" fill="var(--icon-grey)"/></svg>
      Morrow Lane, Ashcombe Vale, Northmere AV12 2JT
    </p>
    <p class="contact contact--phone">
      <svg viewBox="0 0 24 28" aria-hidden="true"><rect x="5" y="4" width="14" height="22" rx="2" fill="none" stroke="var(--icon-grey)" stroke-width="2.2"/><rect x="8" y="7" width="8" height="6" fill="var(--icon-grey)"/><path d="M8 16h2M11 16h2M14 16h2M8 19h2M11 19h2M14 19h2M8 22h2M11 22h2M14 22h2" stroke="var(--icon-grey)" stroke-width="1.6"/><path d="M16 4V0" stroke="var(--icon-grey)" stroke-width="2"/></svg>
      +150963218745
    </p>
    <p class="contact contact--web">
      <svg viewBox="0 0 24 28" aria-hidden="true"><g fill="none" stroke="var(--icon-grey)" stroke-width="1.8"><circle cx="12" cy="14" r="10"/><ellipse cx="12" cy="14" rx="4.5" ry="10"/><path d="M2 14h20M4 9h16M4 19h16"/></g></svg>
      www.corvastudio.com
    </p>
  </article>
</body>
</html>
```